new customer flyer 8.5 X 11 to get people who use CPAP, Snore or have sleep apnea to call us

We sell CPAP equipment and supplies in Ontario. We are designing a flyer for a an advertising campaign encouraging people to switch from the current CPAP supplier to us. Our company name is Breathwell Depot. We are different from a typical CPAP supply store in many ways. A typical store is open 9-5 monday-friday, and the customer must come to the store to get any service. We offer free delivery of supplies of the customer is using the same supplies, so they can just have their supplies shipped rather than come in to pick them up. We also offer free home visits where we will do all the services that can be done in store, including determine the best machine they need, fit them for a mask, set up their equipment and supplies, offer advice, and much more. We also offer night and weekend appointments. Finally we will buy used equipment from our customers and donate this equipment to those in the community who may not be able to afford new equipment, which has 2 benefits of reducing waste and helping the needy.

If you can come up with any other concepts to make us stand out we are open to this.

Our flyer needs to offer a call to action of providing a Prixa Gift card to new customers plus additional call to actions if you are able to create one based on info herein. The gift card amount is $50.00 if this is relevant. We can limit the number available for the promotion if you feel it would encourage a faster and quicker response rate.

The Info needed in the flyer is:
1) Company Name: Breathwell Depot
2) Phone number: 289-517-3064
3) website: www.breathwelldepot-example.com (Make creative in a way that it is easy for user to determine what it says and stimulate them to remember it.)
4) Address is optional, which is 418 Marlow Street, Fort Erie ON L2A 7K3
5) We cover the entire Niagara region and Region of Hamilton in Ontario Canada
6) A call to action is a MUST. We were thinking of using a $50 Prixa gift card for new customers or something else if you feel it would drive more calls to us or more website visits.
7) The objective is to get the customer to call us so we can make them a new customer. The secondary objective is to get the customer to visit our website, because even if they are hesitant to call us, we hope to get them to visit our website and this will give them the confidence to call us.
8) The call to action must encourage a response to hopefully get a call right away. we don't want the customer putting us on the back burner.
9) The flyer is encouraged to not only get people who have sleep apnea, snoring or are currently on CPAP to call, but to also get people who may not suffer from any of these conditions to want to give the flyer to their friends or family who does.
10) I included a bunch of pictures but they are just random pictures, you can use them, use your own or use drawings or whatever to get the message across. You do not need to use all or any of the pictures I provided.
11) We accept all health insurances

I am pretty open, so have fun with the project and be creative as possible!
Updates

There are many designs submitted but many that do not meet the requirements, and many that are similar. I am hoping to find one that does not look like every other generic design, and work with some of the designers who have submitted entries with some potential to modify them into something useable.

Target Market(s)

1) People who snore, have sleep apnea or already use CPAP.
2) Spouses of people snore or have sleep apnea, as these people notice the person who is snoring or having erratic breathing.
3) Friends or family of the people above so that they share the flyer.
4) Focus on 30-60 year old males.

Industry/Entity Type

Advertising

Colors

Designer to choose colors to be used in the design.

Requirements
Must have
• 1) Company Name: Breathwell Depot (Logo can serve as company name as well, files attached)
• 2) Phone number: 289-517-3064
• 3) website: www.breathwelldepot-example.com (Make creative in a way that it is easy for user to determine what it says and stimulate them to remember it.)
• 4) Flyer needs to be friendly and engaging.
• 5) Flyer can be funny or humorous if it will generate customers.
• 6) A call to action is a MUST. We were thinking of using a $50 Prixa gift card for new customers or something else if you feel it would drive more calls to us or more website visits.
• 7) The objective is to get the customer to call us so we can make them a new customer. The secondary objective is to get the customer to visit our website, because even if they are hesitant to call us, we hope to get them to visit our website and this will give them the confidence to call us.
• 8) The call to action must encourage a response to hopefully get a call right away. we don't want the customer putting us on the back burner.
• 9) The flyer is encouraged to not only get people who have sleep apnea, snoring or are currently on CPAP to call, but to also get people who may not suffer from any of these conditions to want to give the flyer to their friends or family who does.
• 10) I included a bunch of pictures but they are just random pictures, you can use them, use your own or use drawings or whatever to get the message across. You do not need to use all or any of the pictures I provided.
• 11) We accept all health insurances
• 12) The FLYER MUST be bold and stand out. This can be with full color, unique text or graphics, or colored backgrounds (Including really bold colors). The point is there is really not a defined market to target with this industry, so any flyers are random location flyers that must be so bold as to grab someones attention such that they want to see what the flyer says.
• 13) Because CPAP only affects about 10-15% of the population, the flyer should be designed that those who snore, suffer from sleep apnea, or CURRENTLY USE CPAP will immediately relate to the flyer and as such want to read it and hopefully call us.
Nice to have
• 1) Address is optional, which is 418 Marlow Street, Fort Erie ON L2A 7K3 (We encourage people to let us come to them, because we offer free shipping and home visits. Therefore our address is not really terribly important.
• 2) We cover the entire Niagara region and Region of Hamilton in Ontario Canada. If they get our flyer they hopefully will call us, however if this can be fit in it confirms that we service the customers area. Without it the customer may wonder if we go to the area where they live.
• 3) Our Taglines are "We make CPAP Personal" and "Better sleep for better health", if they fit into the theme of the designed flyer feel free to add one or both of these.
• 4) The flyer can be designed to appear medical in design if this works, but I prefer fun, engaging and even humorous first, and the medical part becomes secondayry.
Should not have
• 1) The flyer can not be scary or make someone feel uncomfortable.

```html
<!DOCTYPE html>
<html lang="en">
<head>
<meta charset="utf-8">
<title>Breathwell Depot – New Customer Flyer</title>
<link href="https://fonts.googleapis.com/css2?family=Great+Vibes&family=Lato:wght@400;700;900&family=Montserrat:wght@600;700&family=Oswald:wght@500&display=swap" rel="stylesheet">
<style>
  :root {
    --purple: #8e4aa8;
    --purple-dark: #7a3a96;
    --green: #1aad6a;
    --green-dark: #12965a;
    --ink: #3d3d3d;
    --panel: #ececec;
    --page-bg: #e4e1dc;
    --white: #ffffff;
  }
  * { margin: 0; padding: 0; box-sizing: border-box; }
  html, body { width: 1200px; height: 1200px; overflow: hidden; }
  body { background: var(--page-bg); font-family: "Lato", sans-serif; color: var(--ink); position: relative; }

  .flyer {
    position: absolute; left: 197px; top: 30px;
    width: 805px; height: 1140px;
    background: var(--white); overflow: hidden;
    box-shadow: 0 6px 24px rgba(0,0,0,.18);
  }
  .flyer-art { position: absolute; left: 0; top: 0; width: 805px; height: 1140px; }

  .brand {
    position: absolute; left: 46px; top: 92px;
    display: flex; align-items: center; gap: 10px;
    font-family: "Lato", sans-serif; font-weight: 700; font-size: 28px;
    color: var(--green); white-space: nowrap;
  }
  .brand-dot { width: 13px; height: 13px; border-radius: 50%; background: var(--purple); }

  .taglines { position: absolute; right: 50px; top: 44px; text-align: right; font-family: "Montserrat", sans-serif; }
  .tagline-main { font-size: 31px; font-weight: 700; color: var(--purple); line-height: 1.1; letter-spacing: .3px; }
  .tagline-sub { font-size: 22px; font-weight: 700; color: var(--green); line-height: 1.25; margin-top: 2px; }

  .gift-card {
    position: absolute; left: 65px; top: 509px; width: 279px; height: 135px;
    background: linear-gradient(135deg, #fafafa, #eeeeee);
    border: 1px solid #cfcfcf; box-shadow: 0 0 0 3px #fff inset, 0 0 0 4px #d9d9d9 inset;
  }
  .gift-card-bow {
    position: absolute; left: 8px; top: 6px; width: 106px; height: 123px;
    background: radial-gradient(circle at 50% 50%, #a94fb0 0%, #8a2f93 55%, rgba(138,47,147,0) 80%);
  }
  .gift-card-text { position: absolute; left: 116px; right: 6px; top: 20px; text-align: center; }
  .gift-card-get { font-family: "Great Vibes", cursive; font-size: 32px; color: var(--green); line-height: 1; }
  .gift-card-amount { font-family: "Oswald", sans-serif; font-weight: 500; font-size: 24px; color: var(--purple); line-height: 1.25; letter-spacing: .2px; white-space: nowrap; }
  .gift-card-note { font-size: 11px; color: var(--green); margin-top: 4px; white-space: nowrap; }

  .story { position: absolute; left: 46px; top: 673px; width: 310px; }
  .section-rule { height: 1px; background: #c9c9c9; }
  .story-title { font-size: 19px; font-weight: 700; color: var(--purple); margin: 10px 0 10px; }
  .story p { font-size: 12.2px; line-height: 14.6px; text-align: justify; margin-bottom: 14.6px; }

  .insurance { position: absolute; left: 46px; top: 1012px; display: flex; align-items: center; gap: 8px; font-size: 19px; font-weight: 700; color: var(--green); }
  .insurance svg { width: 30px; height: 26px; }

  .offer { position: absolute; left: 415px; top: 680px; width: 342px; }
  .offer-head { display: flex; align-items: center; gap: 6px; }
  .offer-title { font-family: "Montserrat", sans-serif; font-size: 23px; font-weight: 700; color: var(--purple); white-space: nowrap; }
  .offer-head .section-rule { flex: 1; margin-top: 14px; }
  .offer-list { list-style: none; margin-top: 14px; }
  .offer-item { display: flex; gap: 8px; margin-bottom: 13px; }
  .offer-icon { width: 26px; height: 22px; flex: none; margin-top: 1px; }
  .offer-item p { font-size: 12px; line-height: 14.4px; text-align: left; width: 308px; }
  .offer-item strong { color: var(--green); font-weight: 900; }
  .offer-item .phone-inline { color: var(--ink); font-weight: 700; }

  .footer-bar {
    position: absolute; left: 0; top: 1094px; width: 805px; height: 32px;
    background: var(--green);
    color: var(--white); font-size: 12.5px; font-weight: 700;
  }
  .footer-item { position: absolute; top: 0; height: 32px; display: flex; align-items: center; gap: 7px; white-space: nowrap; }
  .footer-item svg { width: 16px; height: 16px; }
  .footer-phone {
    position: absolute; right: 0; top: 1084px; width: 228px; height: 46px;
    background: var(--purple); clip-path: polygon(14px 0, 100% 0, 100% 100%, 0 100%);
    display: flex; align-items: center; gap: 8px; padding-left: 30px;
    color: var(--white); font-size: 23px; font-weight: 700; white-space: nowrap;
  }
  .footer-phone svg { width: 19px; height: 19px; }
  .footer-line { position: absolute; left: 0; top: 1130px; width: 805px; height: 10px; background: var(--purple); }
</style>
</head>
<body>
<main class="flyer">
  <svg class="flyer-art" viewBox="0 0 805 1140">
    <defs>
      <linearGradient id="heroTone" x1="0" y1="0" x2="1" y2="1">
        <stop offset="0" stop-color="#f4f2f0"/>
        <stop offset=".45" stop-color="#d9c2ad"/>
        <stop offset=".75" stop-color="#2f3f6e"/>
        <stop offset="1" stop-color="#eeeef0"/>
      </linearGradient>
      <radialGradient id="portraitTone" cx=".5" cy=".45" r=".6">
        <stop offset="0" stop-color="#d8b6a4"/>
        <stop offset=".7" stop-color="#b99a8c"/>
        <stop offset="1" stop-color="#e8e4e6"/>
      </radialGradient>
      <linearGradient id="panelTone" x1="0" y1="0" x2="0" y2="1">
        <stop offset="0" stop-color="#e6e6e6"/>
        <stop offset="1" stop-color="#f0f0f0"/>
      </linearGradient>
    </defs>

    <rect x="0" y="140" width="805" height="420" fill="url(#heroTone)" role="img" aria-label="Photo of a woman sleeping peacefully on a white pillow while wearing a nasal CPAP mask"/>

    <path d="M0,500 C180,440 420,520 560,535 C660,545 740,520 805,500 L805,1140 L0,1140 Z" fill="var(--white)"/>
    <path d="M0,500 C180,445 330,470 388,492 L388,1023 Q388,1053 358,1053 L0,1053 Z" fill="url(#panelTone)"/>

    <path d="M0,470 C170,420 400,500 560,515 C660,524 740,505 805,478" fill="none" stroke="var(--purple)" stroke-width="7"/>
    <path d="M0,492 C175,435 410,515 560,528 C660,537 740,515 805,492" fill="none" stroke="var(--green)" stroke-width="14"/>

    <circle cx="621" cy="558" r="107" fill="var(--white)" stroke="var(--green)" stroke-width="5"/>
    <circle cx="621" cy="558" r="97" fill="url(#portraitTone)" stroke="var(--purple)" stroke-width="2" role="img" aria-label="Photo of a man asleep wearing a full-face CPAP mask"/>
  </svg>

  <div class="brand"><span class="brand-dot"></span>Breathwell Depot</div>

  <header class="taglines">
    <div class="tagline-main">We make CPAP Personal</div>
    <div class="tagline-sub">and Better sleep for better health</div>
  </header>

  <section class="gift-card">
    <div class="gift-card-bow" role="img" aria-label="Purple satin ribbon bow wrapped around the gift card"></div>
    <div class="gift-card-text">
      <div class="gift-card-get">Get a</div>
      <div class="gift-card-amount">$50 GIFT CARD</div>
      <div class="gift-card-note">for becoming a new customer</div>
    </div>
  </section>

  <section class="story">
    <div class="section-rule"></div>
    <h2 class="story-title">Our Story</h2>
    <p>I have sleep apnea and use CPAP just like you. I work really hard every day to provide for my family, and the last thing I want to do on my time off is run errands, including picking up my CPAP supplies. When I searched for a company that put the customer first, that put service before profits, and that went to the customer instead of making the customer come to them, I came up empty.</p>
    <p>Because I'm a paramedic, and naturally care about people, I felt sad for the people who cannot easily visit their local CPAP suppliers (such as the elderly and the disabled) and determined that the best way to help these people was to open up a sleep therapy store that puts the customer first.</p>
    <p>We believe in helping people, and this should always be first. If you treat your customer right, you will always have customers, and these customers become your friends. When you treat people right, they make your life better.</p>
  </section>

  <div class="insurance">
    <svg viewBox="0 0 30 26"><path d="M15 25 C4 17 1 12 1 7.5 A6.5 6.5 0 0 1 15 5 A6.5 6.5 0 0 1 29 7.5 C29 12 26 17 15 25Z" fill="var(--purple)"/><path d="M18 11h3v3h3v3h-3v3h-3v-3h-3v-3h3z" fill="#fff"/></svg>
    We accept all health insurances.
  </div>

  <section class="offer">
    <div class="offer-head"><h2 class="offer-title">WE OFFER</h2><div class="section-rule"></div></div>
    <ul class="offer-list">
      <li class="offer-item">
        <svg class="offer-icon" viewBox="0 0 26 22"><rect x="1" y="5" width="15" height="10" fill="none" stroke="var(--purple)" stroke-width="1.5"/><path d="M16 8h5l4 4v3h-9z" fill="none" stroke="var(--purple)" stroke-width="1.5"/><circle cx="6" cy="17" r="2" fill="var(--purple)"/><circle cx="20" cy="17" r="2" fill="var(--purple)"/></svg>
        <p><strong>FREE DELIVERY:</strong> So you can spend your time off doing the things you love.</p>
      </li>
      <li class="offer-item">
        <svg class="offer-icon" viewBox="0 0 26 22"><path d="M2 11 L13 2 L24 11" fill="none" stroke="var(--purple)" stroke-width="2"/><rect x="5" y="10" width="16" height="10" fill="var(--purple)"/><rect x="11" y="14" width="4" height="6" fill="#fff"/></svg>
        <p><strong>FREE HOME VISITS:</strong> Because we don't just want to sell you supplies, we want to set them up for you, make sure all your questions are answered, and make sure you get everything you need.</p>
      </li>
      <li class="offer-item">
        <svg class="offer-icon" viewBox="0 0 26 22"><rect x="2" y="2" width="20" height="18" fill="none" stroke="var(--purple)" stroke-width="1.6"/><path d="M2 7h20M6 11h4M12 11h4M6 15h4" stroke="var(--purple)" stroke-width="1.6"/><path d="M20 14v6M17 17h6" stroke="var(--purple)" stroke-width="1.6"/></svg>
        <p><strong>NIGHT AND WEEKEND APPOINTMENTS:</strong> Not everyone works 9-5 Monday through Friday. We offer night and weekend appointments to make sure you can get the service you need on your schedule.</p>
      </li>
      <li class="offer-item">
        <svg class="offer-icon" viewBox="0 0 26 22"><path d="M1 3h4l3 11h13l3-8H7" fill="none" stroke="var(--purple)" stroke-width="1.6"/><path d="M10 6v8M14 6v8M18 6v8" stroke="var(--purple)" stroke-width="1.2"/><circle cx="10" cy="18" r="1.8" fill="var(--purple)"/><circle cx="19" cy="18" r="1.8" fill="var(--purple)"/></svg>
        <p><strong>WE BUY YOUR OLD SUPPLIES :</strong> There are many people who can't afford their supplies, but we want to help them however we can. So part of our commitment to serving everyone is that we buy your gently used equipment, refurbish what we can, and donate it to those who need it.</p>
      </li>
      <li class="offer-item">
        <svg class="offer-icon" viewBox="0 0 26 22"><circle cx="13" cy="7" r="5" fill="none" stroke="var(--purple)" stroke-width="1.5"/><path d="M3 21c1-6 5-8 10-8s9 2 10 8z" fill="none" stroke="var(--purple)" stroke-width="1.5"/></svg>
        <p><strong>PLUS SO MUCH MORE:</strong> Call us at <span class="phone-inline">289-517-3064</span> to speak to a sleep expert who can finally treat you the way you deserve to be treated.</p>
      </li>
    </ul>
  </section>

  <footer>
    <div class="footer-bar">
      <div class="footer-item" style="left:40px">
        <svg viewBox="0 0 18 18"><path d="M1 9 L9 2 L17 9 M4 7v9h4v-5h2v5h4V7" fill="none" stroke="#fff" stroke-width="1.8"/></svg>
        418 Marlow Street, Fort Erie ON L2A 7K3
      </div>
      <div class="footer-item" style="left:318px">
        <svg viewBox="0 0 18 18"><circle cx="9" cy="9" r="7.5" fill="none" stroke="#fff" stroke-width="1.5"/><ellipse cx="9" cy="9" rx="3.5" ry="7.5" fill="none" stroke="#fff" stroke-width="1.3"/><path d="M1.5 9h15M3 5h12M3 13h12" stroke="#fff" stroke-width="1.2"/></svg>
        www.breathwelldepot-example.com
      </div>
    </div>
    <div class="footer-phone">
      <svg viewBox="0 0 20 20"><path d="M4 2l4 1 1 4-2 2c1 2 3 4 5 5l2-2 4 1 1 4-2 2C9 19 1 11 2 4z" fill="#fff"/></svg>
      289-517-3064
    </div>
    <div class="footer-line"></div>
  </footer>
</main>
</body>
</html>
```